Business Card Design Project

Need business card for new non profit organization that includes the attached logo in some form.
with this information
Name: Marcus Holloway Treff
Title: President & Founder
A: P.O. Box 61537, Portland, Oregon, 97451-6153
E: marc@hollowaytrust.org
E: marc@marctreff.com
P: 1.971.555.0172

Industry/Entity Type
Non Profit

```html
<!DOCTYPE html>
<html lang="en">
<head>
<meta charset="utf-8">
<title>Holloway Trust – Business Card</title>
<link rel="stylesheet" href="https://fonts.googleapis.com/css2?family=Open+Sans:wght@400;700&display=swap">
<style>
  :root {
    --navy: #233068;
    --gold: #e8ae25;
    --white: #ffffff;
    --backdrop: #e6e7ea;
  }
  html, body {
    margin: 0;
    padding: 0;
    width: 1200px;
    height: 900px;
    overflow: hidden;
    background: var(--backdrop);
    font-family: "Open Sans", Arial, sans-serif;
  }
  .card {
    position: absolute;
    left: 180px;
    top: 210px;
    width: 840px;
    height: 480px;
    background: var(--white);
    overflow: hidden;
    box-shadow: 0 10px 30px rgba(0,0,0,0.18);
  }
  .card-wave {
    position: absolute;
    inset: 0;
    width: 840px;
    height: 480px;
  }
  .brand {
    position: absolute;
    left: 470px;
    top: 70px;
    width: 300px;
    text-align: center;
    color: var(--navy);
    font-weight: 700;
    font-size: 34px;
    letter-spacing: 0.5px;
  }
  .identity {
    position: absolute;
    left: 42px;
    top: 178px;
  }
  .identity-name {
    margin: 0;
    color: var(--navy);
    font-weight: 700;
    font-size: 22px;
    text-transform: uppercase;
    letter-spacing: 0.2px;
  }
  .identity-title {
    margin: 2px 0 0;
    color: var(--gold);
    font-size: 15px;
  }
  .contact {
    position: absolute;
    left: 50px;
    top: 350px;
    margin: 0;
    padding: 0;
    list-style: none;
    color: var(--white);
    font-size: 17px;
    line-height: 26px;
  }
  .contact-label {
    color: var(--gold);
  }
</style>
</head>
<body>
  <section class="card">
    <svg class="card-wave" viewBox="0 0 840 480" aria-hidden="true">
      <path fill="var(--gold)" d="M0,330 C60,270 200,270 480,262 C650,254 760,200 840,90 L840,112 C760,222 650,276 480,284 C200,292 60,292 0,356 Z"/>
      <path fill="var(--navy)" d="M0,366 C60,306 200,304 480,294 C650,286 760,236 840,130 L840,480 L0,480 Z"/>
    </svg>

    <div class="brand">Holloway Trust</div>

    <div class="identity">
      <h1 class="identity-name">Marcus Holloway Treff</h1>
      <p class="identity-title">President &amp; Founder</p>
    </div>

    <ul class="contact">
      <li><span class="contact-label">P:</span> 1.971.555.0172</li>
      <li><span class="contact-label">E:</span> marc@marctreff.com</li>
      <li><span class="contact-label">E:</span> marc@hollowaytrust.org</li>
      <li><span class="contact-label">A:</span> P.O. Box 61537, Portland, Oregon, 97451-6153</li>
    </ul>
  </section>
</body>
</html>
```